Poster Design Project

We need a poster designed for of range of products, We would like the 7 suitcases on a police line up style wall, maybe a brick style and they are in the spotlight with a heading of The Unusual Suspects.. then smaller maybe along the bottom Not All Luggage Is The Same.. Stand Out From the Crowd..
I have the images of the cases and need this soon, it must be modern and very cool looking. let me know if you have any questions.
Target Market(s)
this is for Ladies 15 - 55 or store owners.
Industry/Entity Type
Crowd
Look and feel

```html
<!DOCTYPE html>
<html lang="en">
<head>
<meta charset="utf-8">
<title>The Unusual Suspects</title>
<link rel="stylesheet" href="https://fonts.googleapis.com/css2?family=Open+Sans:wght@600;700&display=swap">
<style>
  :root {
    --teal: #4595b4;
    --white: #ffffff;
    --rule: #7d7d7d;
    --label: #7a7a7a;
  }
  html, body {
    margin: 0;
    padding: 0;
    overflow: hidden;
    background: var(--white);
  }
  .poster {
    position: relative;
    width: 848px;
    height: 1200px;
    overflow: hidden;
    background: var(--white);
    font-family: "Open Sans", Arial, sans-serif;
  }
  .band {
    position: absolute;
    left: 0;
    width: 100%;
    background: var(--teal);
  }
  .band--top { top: 0; height: 331px; }
  .band--bottom { top: 795px; height: 405px; }

  .headline {
    position: absolute;
    top: 150px;
    left: 0;
    width: 100%;
    margin: 0;
    text-align: center;
    color: var(--white);
    font-weight: 700;
    font-size: 50px;
    letter-spacing: 1px;
    line-height: 1;
  }
  .headline__key { font-size: 66px; }

  .height-chart {
    position: absolute;
    left: 0;
    top: 0;
    width: 848px;
    height: 1200px;
  }
  .height-chart line {
    stroke: var(--rule);
    stroke-width: 2.5;
  }
  .height-chart text {
    fill: var(--label);
    font-family: "Open Sans", Arial, sans-serif;
    font-weight: 700;
    font-size: 26px;
    letter-spacing: 1px;
  }

  .case {
    position: absolute;
    border-radius: 14px;
    box-shadow: 0 3px 6px rgba(0,0,0,0.25);
  }
  .case::before {
    content: "";
    position: absolute;
    top: -28px;
    left: 50%;
    width: 54px;
    height: 28px;
    margin-left: -27px;
    border: 5px solid #2f2f2f;
    border-bottom: none;
    box-sizing: border-box;
  }
  .case--city     { left: 100px; top: 505px; width: 116px; height: 245px; background: linear-gradient(160deg, #cfcfcf, #5c5c5c 55%, #2a2a2a); }
  .case--stripes  { left: 372px; top: 532px; width: 128px; height: 212px; background: linear-gradient(90deg, #c94a2b, #2e6f9e 35%, #e7a23a 65%, #2b4f7a); }
  .case--pearl    { left: 474px; top: 518px; width: 90px;  height: 222px; background: linear-gradient(180deg, #ffffff, #d8dde2); }
  .case--speaker  { left: 563px; top: 486px; width: 156px; height: 254px; background: linear-gradient(90deg, #2a2623, #4b4541 50%, #1f1c1a); }
  .case--sky      { left: 212px; top: 513px; width: 160px; height: 210px; background: linear-gradient(180deg, #bcd6ec, #93b7d8); }
  .case--washer   { left: 372px; top: 556px; width: 106px; height: 188px; background: linear-gradient(180deg, #ffffff, #dfe3e6); }
  .case--tower    { left: 523px; top: 540px; width: 130px; height: 208px; background: linear-gradient(180deg, #f4f4f4, #9a9a9a 60%, #3b3b3b); }
  .case--flag     { left: 168px; top: 640px; width: 248px; height: 388px; border-radius: 18px; background: radial-gradient(circle at 50% 45%, #c8322a 0%, #b3362b 22%, #d8b37a 34%, #2a3d82 55%, #142866 100%); }
  .case--sky::before,
  .case--washer::before,
  .case--tower::before { display: none; }

  .tagline {
    position: absolute;
    left: 316px;
    top: 1002px;
    margin: 0;
    color: var(--white);
    font-weight: 700;
    line-height: 1.55;
  }
  .tagline__lead { display: block; font-size: 29px; }
  .tagline__call { display: block; font-size: 30px; letter-spacing: 0.5px; }
</style>
</head>
<body>
  <main class="poster">
    <div class="band band--top"></div>
    <div class="band band--bottom"></div>

    <h1 class="headline">THE <span class="headline__key">UNUSUAL</span> SUSPECTS</h1>

    <svg class="height-chart" viewBox="0 0 848 1200" aria-hidden="true">
      <line x1="37" y1="384" x2="783" y2="384"/>
      <line x1="37" y1="431" x2="783" y2="431"/>
      <line x1="37" y1="477" x2="783" y2="477"/>
      <line x1="37" y1="522" x2="783" y2="522"/>
      <line x1="37" y1="568" x2="783" y2="568"/>
      <line x1="37" y1="613" x2="783" y2="613"/>
      <line x1="37" y1="659" x2="783" y2="659"/>
      <text x="42" y="422">6’0’’</text><text x="713" y="422">6’0’’</text>
      <text x="42" y="468">5’0’’</text><text x="713" y="468">5’0’’</text>
      <text x="42" y="514">4’0’’</text><text x="713" y="514">4’0’’</text>
      <text x="42" y="559">3’0’’</text><text x="713" y="559">3’0’’</text>
      <text x="42" y="605">2’0’’</text><text x="713" y="605">2’0’’</text>
      <text x="42" y="650">1’0’’</text><text x="713" y="650">1’0’’</text>
    </svg>

    <div class="case case--city" role="img" aria-label="Hard-shell suitcase printed with a black and white city street scene"></div>
    <div class="case case--stripes" role="img" aria-label="Suitcase with bold multicoloured stripes"></div>
    <div class="case case--pearl" role="img" aria-label="Glossy white suitcase with a printed landmark"></div>
    <div class="case case--speaker" role="img" aria-label="Dark wood-effect suitcase printed with a loudspeaker"></div>
    <div class="case case--sky" role="img" aria-label="Pale blue retro suitcase"></div>
    <div class="case case--washer" role="img" aria-label="White suitcase printed as a washing machine"></div>
    <div class="case case--tower" role="img" aria-label="Suitcase printed with a black and white photo of the Eiffel Tower"></div>
    <div class="case case--flag" role="img" aria-label="Large suitcase printed with a weathered Union Jack, stepping forward from the line-up"></div>

    <p class="tagline">
      <span class="tagline__lead">Not all luggage is the same</span>
      <span class="tagline__call">STAND OUT OF THE CROWD</span>
    </p>
  </main>
</body>
</html>
```